Pilates Classes Flyer Design

I need a flyer designed that will promote my range of classes held in Bath, UK. I teach beginners, intermediate level and Over 50's and 60's and also teach individuals in their own homes. I would like to see designs using my colours blue Pantone 306 and Lime Green 14-0452 TPX TCX. The flyer should reflect a friendly, welcoming and professional class structure. I attach an old flyer for your reference and copy.

Target Market(s)

Men and Women who have busy lives working hard, who recognise they need to stretch out, do some exercise and de-stress after a busy day

Ladies over 50 who want to do some Pilates in a friendly fun environment and meet people at the same time.

Industry/Entity Type

It Professional

Font styles to use
Sans Serif
Script

Requirements
Must have
• One-sided flyer
Text only logo. Drop the figure

```html
<!DOCTYPE html>
<html lang="en">
<head>
<meta charset="utf-8">
<title>CoreFlow Pilates – Classes Flyer</title>
<link rel="stylesheet" href="https://fonts.googleapis.com/css2?family=Fira+Sans+Condensed:wght@600;700&family=Montserrat:wght@700&display=swap">
<style>
  :root {
    --paper: #f3ede6;
    --lime: #b1e41c;
    --cyan: #4fd8ee;
    --band-grey: #555759;
    --ink: #111111;
    --badge-blue: #3f93b8;
  }
  * { margin: 0; padding: 0; box-sizing: border-box; }
  html, body { width: 851px; height: 1200px; overflow: hidden; background: var(--paper); }
  .flyer { position: relative; width: 851px; height: 1200px; background: var(--paper); overflow: hidden;
    font-family: "Fira Sans Condensed", "Arial Narrow", sans-serif; }

  .top-band { position: absolute; left: 0; top: 45px; width: 851px; height: 80px; background: var(--band-grey);
    display: flex; justify-content: center; align-items: center; }
  .brand-name { font-weight: 700; font-size: 54px; line-height: 1; color: var(--lime); letter-spacing: 1px; }

  .photo-frame { position: absolute; left: 323px; top: 195px; width: 515px; height: 341px; border: 6px solid var(--lime);
    background: linear-gradient(160deg, #e9e6df 0%, #cfccc4 45%, #4a4a52 70%, #9fd3e3 100%); }

  .headline { position: absolute; left: 22px; top: 221px; font-weight: 700; font-size: 37px; line-height: 44px; color: var(--lime); white-space: nowrap; }
  .intro { position: absolute; left: 22px; top: 314px; font-weight: 700; font-size: 22px; line-height: 31px; color: var(--cyan); white-space: nowrap; }
  .offer { position: absolute; left: 18px; top: 508px; width: 290px; text-align: center; font-weight: 700; font-size: 23px; line-height: 32px; color: var(--cyan); white-space: nowrap; }
  .quality { position: absolute; left: 356px; top: 550px; font-weight: 700; font-size: 19.5px; line-height: 28px; color: var(--lime); white-space: nowrap; }

  .venues-title { position: absolute; left: 28px; top: 730px; font-weight: 700; font-size: 29px; line-height: 36px; color: var(--ink); white-space: nowrap; }
  .venue { position: absolute; left: 28px; white-space: nowrap; }
  .venue-name { font-weight: 700; font-size: 33px; line-height: 40px; color: var(--lime); }
  .venue-times { font-weight: 600; font-size: 21px; line-height: 28px; color: var(--ink); }

  .badge { position: absolute; left: 546px; top: 874px; width: 274px; height: 92px; border-radius: 9px; background: var(--badge-blue); }

  .call { position: absolute; left: 0; width: 851px; top: 1022px; text-align: center;
    font-family: "Montserrat", sans-serif; font-weight: 700; font-size: 41px; line-height: 50px; letter-spacing: 2px; color: var(--ink); }
  .phone { position: absolute; left: 0; width: 851px; top: 1072px; display: flex; justify-content: center; align-items: center; gap: 14px;
    font-family: "Montserrat", sans-serif; font-weight: 700; font-size: 50px; line-height: 60px; letter-spacing: 4px; color: var(--cyan); }
  .email-band { position: absolute; left: 0; top: 1131px; width: 851px; height: 69px; background: var(--lime);
    display: flex; justify-content: center; align-items: center;
    font-weight: 700; font-size: 36px; letter-spacing: 5px; color: var(--ink); text-transform: uppercase; white-space: nowrap; }
</style>
</head>
<body>
<main class="flyer">
  <header class="top-band">
    <h1 class="brand-name">CoreFlow Pilates</h1>
  </header>

  <div class="photo-frame" role="img" aria-label="Photo of an older woman in black exercise clothes doing a kneeling Pilates move on a blue mat"></div>

  <h2 class="headline">New classes<br>near you!</h2>
  <p class="intro">Pilates is for EVERYONE<br>whatever level of fitness,<br>age or ability to help you<br>build strength, flexibility<br>and overall well-being.</p>

  <p class="offer">I teach beginners,<br>intermediate level<br>and Over 50's and<br>60's and also teach<br>individuals in their<br>own homes</p>

  <p class="quality">Quality teaching with Balanced Core Method<br>Teacher. Progressive approach. Teaching good<br>movement skills. Small class sizes and friendly<br>atmosphere. Beginners, Intermediate and<br>Over 50’s classes to choose from.</p>

  <h3 class="venues-title">Join my one-hour classes at:</h3>
  <div class="venue" style="top:778px">
    <p class="venue-name">St Aidan’s Church Hall, Elm Rise</p>
    <p class="venue-times">Monday evenings, Tuesday and Friday mornings</p>
  </div>
  <div class="venue" style="top:856px">
    <p class="venue-name">Linden Park Dr. Surgery</p>
    <p class="venue-times">Tuesday evenings</p>
  </div>
  <div class="venue" style="top:934px">
    <p class="venue-name">Harwood Centre, Kingsley Road</p>
    <p class="venue-times">Wednesday mornings and evenings</p>
  </div>

  <div class="badge" role="img" aria-label="Teacher certification badge"></div>

  <p class="call">Call Tessa on</p>
  <p class="phone">
    <svg width="48" height="48" viewBox="0 0 48 48" aria-hidden="true">
      <circle cx="24" cy="24" r="21" fill="none" stroke="var(--cyan)" stroke-width="3"/>
      <path d="M17 13c2 0 3 4 4 6 0 1-2 2-2 3 1 3 4 6 7 7 1 0 2-2 3-2 2 1 6 2 6 4 0 2-2 4-4 4-9 0-18-9-18-18 0-2 2-4 4-4z" fill="var(--cyan)"/>
    </svg>
    <span>07700900123</span>
  </p>

  <footer class="email-band">tessa.marlow@example.co.uk</footer>
</main>
</body>
</html>
```